Logo & Website Reference Design for "PineRidge.Trips"

Hi there!

I like to get a logo, website incl. fonts reference design for "Pine Ridge Trips". The URL will be PineRidge.Trips or Pine-Ridge.Trips and would like to have a memorable symbol, too. Basically, the symbol should not be a OffRoad car rather than e.g. Mountains, Trails, skid-marks etc.. The website and activities I will provide video documented of off-road trails with off-road cars; mainly off-road campers and POI's will be mentioned online. Not "extreme Off-Road" folks with their Brakmor Valiants or Quillet Roamers rather than more mainstream. It would be great if you could consider Halvenau Camper Vans (modern, K3 or K4) that are offroad capable (higher, extreme tires, snorkel etc.).

If you work on the sample images for the website, pls make use of e.g. off-road trails (gravel roads) thru forest, mountains, rocks etc. - no street roads.

Also, I am planning to manage the website content with plimo.example - if you have any experience - much appreciated. Alternatively, I am also happy with e.g. PageKilnly to manage the content in the close future on my onwn.

Target Market(s)

Key target audience are mainly male people in Central- Northern- and Benelux Europe in the age of 28 - 55 years.

Industry/Entity Type

Tourism

Logo Text

Pine-Ridge.Trips or PineRidge.Trips (please recommend with "-" or w/o)

Number of Pages Required

4 page

Font styles to use
Sans Serif

Colors

Designer to choose colors to be used in the design.

Requirements
Must have
• Modern and attractive logo with symbol that works w/o text (PineRidge.Trips).
• Webdesign must work on mobile devices (responsive) as well as on computer browsers
Nice to have
• Even if URL is PineRidge.Trips and/or Pine-Ridge.Trips the sub-slogan could be used e.g. real off-road tours | virtual
• Favicon for website

```html
<!DOCTYPE html>
<html lang="en">
<head>
<meta charset="utf-8">
<title>PineRidge.Trips</title>
<link rel="stylesheet" href="https://fonts.googleapis.com/css2?family=Raleway:wght@400;500;600;700;800;900&family=Architects+Daughter&display=swap">
<style>
:root{
  --orange:#f07a12;
  --orange-deep:#e85d04;
  --orange-light:#f7941d;
  --ink:#222;
  --muted:#888;
  --white:#fff;
  --panel:rgba(48,44,40,.82);
  --line:#333;
}
*{box-sizing:border-box;margin:0;padding:0}
html,body{width:1200px;height:4035px;overflow:hidden;background:var(--white);font-family:"Raleway",sans-serif;color:var(--ink)}
.page{position:relative;width:1200px;height:4035px}
.abs{position:absolute}

/* header */
.site-header{left:0;top:0;width:1200px;height:77px;background:var(--white)}
.brand{left:125px;top:14px;display:flex;align-items:center;gap:10px}
.brand-mark{width:50px;height:50px;border-radius:50%;border:3px solid var(--ink)}
.brand-name{font-weight:800;font-size:17px;color:var(--orange);letter-spacing:.2px}
.brand-sub{font-size:9px;color:var(--ink);margin-top:1px}
.main-nav{top:33px;left:0;width:1200px;font-size:13px;font-weight:500;letter-spacing:.6px}
.main-nav span{position:absolute}

/* hero */
.hero{left:0;top:77px;width:1200px;height:620px;background:linear-gradient(180deg,#8fb3d8 0%,#c9d6df 22%,#6f9a3c 42%,#5c8a2b 62%,#9a8a62 85%,#7c6b4a 100%)}
.hero-title{left:668px;top:275px;font-family:"Architects Daughter",cursive;font-size:76px;color:var(--white);line-height:1}
.hero-tag{left:793px;top:367px;background:var(--orange);color:var(--white);font-weight:700;font-size:25px;padding:1px 7px;line-height:1.1}
.arrow{width:22px;height:42px}
.dots{display:flex;gap:8px}
.dot{width:8px;height:8px;border-radius:50%;border:1px solid var(--white)}
.dot.on{background:var(--white)}

/* promo */
.promo{left:0;top:697px;width:1200px;height:454px;background:linear-gradient(100deg,#f28a1a 0%,#ef7a10 45%,#e96506 100%)}
.promo-art{left:330px;top:56px;width:870px;height:398px;background:radial-gradient(ellipse at 70% 55%,rgba(60,50,40,.35),rgba(240,120,20,0) 60%)}
.promo-copy{left:186px;top:131px;color:var(--white)}
.promo-copy .l1{font-size:29px;font-weight:500}
.promo-copy .l2{font-size:43px;font-weight:900;letter-spacing:-.5px;line-height:1.1}
.promo-copy .l3{font-size:29px;font-weight:500}
.btn-light{display:inline-block;margin-top:17px;background:var(--white);color:var(--orange-deep);font-weight:700;font-size:14px;padding:9px 25px;letter-spacing:.3px}

/* featured */
.section-title{left:0;width:1200px;text-align:center;font-family:"Architects Daughter",cursive;font-size:42px;color:var(--ink)}
.filters{left:0;top:1313px;width:1200px;text-align:center;font-size:15px;color:var(--muted)}
.filters .active{color:var(--orange);font-weight:700}
.filters .sep{margin:0 10px;color:#666}
.tour-card{width:574px;height:509px;overflow:hidden}
.tour-info{position:absolute;left:0;top:243px;width:276px;height:266px;background:var(--panel);color:var(--white);padding:28px 0 0 31px}
.tour-name{font-size:21px;font-weight:600}
.tour-meta{font-size:14px;margin-top:2px}
.tour-meta b{color:var(--orange)}
.tour-meta span{color:var(--orange);opacity:.75;font-weight:500}
.tour-desc{font-size:13.4px;line-height:1.3;margin-top:18px;width:215px}
.play{position:absolute;left:31px;top:202px;width:38px;height:38px}
.btn-outline{left:493px;top:3016px;width:212px;height:36px;border:2px solid var(--ink);font-size:14px;display:flex;align-items:center;justify-content:center}

/* testimonials */
.testimonials{left:0;top:3149px;width:1200px;height:490px;background:linear-gradient(180deg,#f28c1c 0%,#ee7a12 50%,#e8680a 100%)}
.testi-title{top:90px;font-size:40px;color:var(--white)}
.testi-photo{left:231px;top:162px;width:192px;height:192px;border-radius:50%;background:radial-gradient(circle at 40% 40%,#8d9aa8,#4b5562)}
.testi-text{left:451px;top:188px;width:540px;color:var(--white);font-size:13.6px;line-height:1.27}
.testi-name{margin-top:10px;font-weight:700;font-size:17px}

/* mailing */
.signup{left:418px;top:3730px;width:364px}
.signup h3{font-size:17px;font-weight:700;text-align:center}
.signup .field{margin-top:18px;font-size:13px;padding-bottom:6px;border-bottom:1px solid var(--line)}
.btn-dark{margin-top:32px;height:36px;background:#000;color:var(--white);font-size:13px;font-weight:600;display:flex;align-items:center;justify-content:center}
.social{left:563px;top:3956px;display:flex;gap:17px}
.social i{display:block;width:12px;height:12px;border-radius:50%;background:#111}
.copyright{left:0;top:3994px;width:1200px;text-align:center;font-size:9px;color:#333}
</style>
</head>
<body>
<div class="page">

<header class="site-header abs">
  <div class="brand abs">
    <div class="brand-mark"></div>
    <div>
      <div class="brand-name">PineRidge.Trips</div>
      <div class="brand-sub">real off-road tours | virtual</div>
    </div>
  </div>
  <nav class="main-nav abs">
    <span style="left:732px">HOME</span>
    <span style="left:798px">TOURS</span>
    <span style="left:871px">HOW IT WORKS</span>
    <span style="left:1000px">CONTACT</span>
  </nav>
</header>

<section class="hero abs" role="img" aria-label="Camper van on a gravel trail through green hills and forest">
  <svg class="arrow abs" style="left:45px;top:275px" viewBox="0 0 22 42"><path d="M20 2 2 21l18 19" fill="none" stroke="#fff" stroke-width="2"/></svg>
  <svg class="arrow abs" style="left:1133px;top:275px" viewBox="0 0 22 42"><path d="M2 2l18 19L2 40" fill="none" stroke="#fff" stroke-width="2"/></svg>
  <div class="dots abs" style="left:579px;top:572px"><i class="dot on"></i><i class="dot"></i><i class="dot"></i></div>
</section>
<div class="hero-title abs">Explore</div>
<div class="hero-tag abs">the best routes</div>

<section class="promo abs">
  <div class="promo-art abs" role="img" aria-label="Camper van in orange tint and a hand holding a phone playing a tour video"></div>
  <div class="promo-copy abs">
    <div class="l1">Top-quality videos of</div>
    <div class="l2">real off-road tours</div>
    <div class="l3">always on your fingertips</div>
    <div class="btn-light">EXPLORE TOURS</div>
  </div>
</section>

<h2 class="section-title abs" style="top:1250px">Featured Tours</h2>
<div class="filters abs"><span class="active">All</span><span class="sep">|</span>Relaxed<span class="sep">|</span>Intermediate<span class="sep">|</span>Expert</div>

<article class="tour-card abs" style="left:17px;top:1391px;background:linear-gradient(180deg,#8eb0d9 0%,#a8c0dc 40%,#8a7a66 65%,#a79d90 100%)" role="img" aria-label="Rocky desert riverbed between mountains">
  <div class="tour-info"><div class="tour-name">Northlake swamps</div><div class="tour-meta"><b>Expert</b> | <span>3-4 days</span></div><div class="tour-desc">SEO text Lorem ipsum dolor sit amet, consectet adipiscing elit. Donec cursus leo lobortis augue ultricies, et consequat enim fermentum.</div>
  <svg class="play" viewBox="0 0 38 38"><circle cx="19" cy="19" r="19" fill="#f07a12"/><path d="M15 11l12 8-12 8z" fill="#fff"/></svg></div>
</article>
<article class="tour-card abs" style="left:609px;top:1391px;width:573px;background:linear-gradient(180deg,#3d5a2a 0%,#5f7e3c 45%,#4a5530 75%,#6d5a3e 100%)" role="img" aria-label="Dirt trail through dense green forest">
  <div class="tour-info"><div class="tour-name">Northlake swamps</div><div class="tour-meta"><b>Expert</b> | <span>3-4 days</span></div><div class="tour-desc">SEO text Lorem ipsum dolor sit amet, consectet adipiscing elit. Donec cursus leo lobortis augue ultricies, et consequat enim fermentum.</div>
  <svg class="play" viewBox="0 0 38 38"><circle cx="19" cy="19" r="19" fill="#f07a12"/><path d="M15 11l12 8-12 8z" fill="#fff"/></svg></div>
</article>

<article class="tour-card abs" style="left:17px;top:1919px;background:linear-gradient(180deg,#3f6e2c 0%,#5a8c3a 35%,#2f4c5e 60%,#8aa0a8 80%,#4d6b30 100%)" role="img" aria-label="River meeting the sea under green cliffs">
  <div class="tour-info"><div class="tour-name">Northlake swamps</div><div class="tour-meta"><b>Intermediate</b> | <span>1-2 days</span></div><div class="tour-desc">SEO text Lorem ipsum dolor sit amet, consectet adipiscing elit. Donec cursus leo lobortis augue ultricies, et consequat enim fermentum.</div>
  <svg class="play" viewBox="0 0 38 38"><circle cx="19" cy="19" r="19" fill="#f07a12"/><path d="M15 11l12 8-12 8z" fill="#fff"/></svg></div>
</article>
<article class="tour-card abs" style="left:609px;top:1919px;width:573px;background:linear-gradient(180deg,#c9d4dc 0%,#dfe3e2 25%,#8a6e56 45%,#a7846a 75%,#b08e70 100%)" role="img" aria-label="Off-road car on a dirt track below a bare hill">
  <div class="tour-info"><div class="tour-name">Northlake swamps</div><div class="tour-meta"><b>Relaxed</b> | <span>5-6 days</span></div><div class="tour-desc">SEO text Lorem ipsum dolor sit amet, consectet adipiscing elit. Donec cursus leo lobortis augue ultricies, et consequat enim fermentum.</div>
  <svg class="play" viewBox="0 0 38 38"><circle cx="19" cy="19" r="19" fill="#f07a12"/><path d="M15 11l12 8-12 8z" fill="#fff"/></svg></div>
</article>

<article class="tour-card abs" style="left:17px;top:2449px;width:575px;background:linear-gradient(180deg,#2f4a2a 0%,#5d5a3c 35%,#8a7656 60%,#b29a72 100%)" role="img" aria-label="Off-road car driving through a muddy jungle track">
  <div class="tour-info"><div class="tour-name">Northlake swamps</div><div class="tour-meta"><b>Expert</b> | <span>3-4 days</span></div><div class="tour-desc">SEO text Lorem ipsum dolor sit amet, consectet adipiscing elit. Donec cursus leo lobortis augue ultricies, et consequat enim fermentum.</div>
  <svg class="play" viewBox="0 0 38 38"><circle cx="19" cy="19" r="19" fill="#f07a12"/><path d="M15 11l12 8-12 8z" fill="#fff"/></svg></div>
</article>
<article class="tour-card abs" style="left:609px;top:2449px;width:573px;height:512px;background:linear-gradient(180deg,#cfd6d6 0%,#6d8a5a 30%,#4f7a3c 60%,#6a7a5e 100%)" role="img" aria-label="Winding mountain pass road in a green valley">
  <div class="tour-info"><div class="tour-name">Northlake swamps</div><div class="tour-meta"><b>Relaxed</b> | <span>3-4 days</span></div><div class="tour-desc">SEO text Lorem ipsum dolor sit amet, consectet adipiscing elit. Donec cursus leo lobortis augue ultricies, et consequat enim fermentum.</div>
  <svg class="play" viewBox="0 0 38 38"><circle cx="19" cy="19" r="19" fill="#f07a12"/><path d="M15 11l12 8-12 8z" fill="#fff"/></svg></div>
</article>

<div class="btn-outline abs">View More Tours</div>

<section class="testimonials abs" role="img" aria-label="Orange-tinted mountain landscape">
  <h2 class="section-title testi-title abs">Testimonials</h2>
  <svg class="arrow abs" style="left:122px;top:235px" viewBox="0 0 22 42"><path d="M20 2 2 21l18 19" fill="none" stroke="#fff" stroke-width="2"/></svg>
  <svg class="arrow abs" style="left:1062px;top:235px" viewBox="0 0 22 42"><path d="M2 2l18 19L2 40" fill="none" stroke="#fff" stroke-width="2"/></svg>
  <div class="testi-photo abs" role="img" aria-label="Portrait of two travellers in a car"></div>
  <div class="testi-text abs">
    Lorem ipsum dolor sit amet, consectetur adipiscing elit. Donec cursus leo lobortis augue ultricies, et consequat enim fermentum. SEO text Lorem ipsum dolor sit amet, consectetur adipiscing elit. Donec cursus leo lobortis augue ultricies, et consequat enim fermentum. SEO text Lorem ipsum dolor sit amet, consectetur adipiscing elit. Donec cursus leo lobortis augue ultricies, et consequat enim fermentum. SEO text Lorem ipsum dolor sit amet, consectetur adipiscing elit. Donec cursus leo lobortis augue ultricies, et consequat enim fermentum.
    <div class="testi-name">- Tomas &amp; Henrik</div>
  </div>
  <div class="dots abs" style="left:561px;top:413px"><i class="dot"></i><i class="dot"></i><i class="dot on"></i><i class="dot"></i><i class="dot"></i></div>
</section>

<section class="signup abs">
  <h3>Don't miss tour! Join our mailing list today!</h3>
  <div class="field">Enter you email here</div>
  <div class="btn-dark">Subscribe Now</div>
</section>

<div class="social abs" aria-label="Social links"><i></i><i></i><i></i></div>
<div class="copyright abs">© 2020 PineRidge.Trips &nbsp;|&nbsp; All Rights reserved</div>

</div>
</body>
</html>
```